Web Pages Improvement, Update of existing MIRB website

Redesign existing website www.mirb.asn.au The # of pages can be reduced to a total of 6 including the home page. We have a design project out for the logo for this site so feel free to bid for that also.
As this is a simple brief with basic pages, we expect the end result to be code ready for uploaded to our existing host.

```html
<!DOCTYPE html>
<html lang="en">
<head>
<meta charset="utf-8">
<title>MIRB – Measurement Integrity Review Board</title>
<link href="https://fonts.googleapis.com/css2?family=Open+Sans:wght@400;600&display=swap" rel="stylesheet">
<style>
:root{
  --page:#e3e3e3;
  --white:#ffffff;
  --orange:#f47a12;
  --orange-dark:#c65300;
  --gold:#d9aa3a;
  --gold-light:#e9c660;
  --gold-text:#6b5424;
  --cream:#fdecc8;
  --body-text:#5e5e5e;
  --ink:#111111;
  --tile-border:#d2d2d2;
}
*{box-sizing:border-box;margin:0;padding:0}
html,body{width:1200px;height:969px;overflow:hidden}
body{background:var(--page);font-family:"Open Sans",Verdana,sans-serif;position:relative}
.topbar{position:absolute;left:0;top:0;width:1200px;height:57px;background:linear-gradient(#ececec,#dcdcdc)}
.contact-line{position:absolute;right:60px;top:17px;display:flex;gap:16px;font-size:14.5px;color:var(--orange)}
.contact-line span{display:flex;align-items:center;gap:6px}
.banner{position:absolute;left:0;top:57px;width:1200px;height:292px;background:linear-gradient(90deg,var(--gold) 0%,var(--gold-light) 100%)}
.banner-art{position:absolute;left:0;top:0}
.logo-box{position:absolute;left:59px;top:0;width:249px;height:110px;background:var(--white);box-shadow:0 6px 8px rgba(0,0,0,.18);display:flex;align-items:center;justify-content:center}
.logo-name{font-size:52px;font-weight:400;color:var(--orange);letter-spacing:4px}
.org-title{position:absolute;left:89px;top:180px;font-size:23px;font-weight:600;color:var(--gold-text);line-height:33px}
.nav{position:absolute;left:59px;top:301px;width:1081px;height:46px;background:linear-gradient(#e8720c,#c65300);border-radius:3px 3px 0 0;display:flex}
.nav a{color:var(--white);text-decoration:none;font-size:17px;padding:0 8px 0 13px;line-height:46px;border-right:1px solid #a94600}
.nav a:last-child{border-right:none}
.rule{position:absolute;left:0;top:348px;width:1200px;height:2px;background:var(--orange)}
.content{position:absolute;left:59px;top:351px;width:1081px;height:552px;background:var(--white);border-radius:0 0 4px 4px}
.section-head{position:absolute;height:48px;background:var(--cream);color:var(--orange);font-size:21px;line-height:48px;padding-left:9px}
.welcome-head{left:14px;top:23px;width:687px}
.members-head{left:735px;top:23px;width:318px}
.intro{position:absolute;left:15px;top:84px;width:687px;font-size:12.6px;line-height:19.6px;color:var(--body-text);text-align:justify;letter-spacing:.15px}
.intro p{margin-bottom:19.6px}
.tile{position:absolute;width:99px;height:87px;border:1px solid var(--tile-border);border-radius:4px;display:flex;align-items:center;justify-content:center;gap:5px;font-size:14px;color:#1d4a9b}
.tile i{display:block;width:12px;height:12px;background:#1d4a9b;border-radius:50%}
.footer{position:absolute;left:61px;top:918px;font-size:12px;line-height:15.5px;color:var(--ink)}
.marks{position:absolute;right:60px;top:918px;display:flex;gap:16px}
</style>
</head>
<body>
<header class="topbar">
  <div class="contact-line">
    <span><svg width="22" height="16" viewBox="0 0 22 16"><path d="M2 5c3-4 15-4 18 0l-1 3h-4l-1-2H8L7 8H3z" fill="#9a9a9a"/><rect x="5" y="9" width="12" height="6" rx="1" fill="#9a9a9a"/></svg>+61 (0)3 9000 4172</span>
    <span><svg width="20" height="15" viewBox="0 0 20 15"><rect x="1" y="1" width="18" height="13" fill="none" stroke="#9a9a9a" stroke-width="1.5"/><path d="M1 1l9 7 9-7" fill="none" stroke="#9a9a9a" stroke-width="1.5"/></svg>secretariat@mirb.com.au</span>
  </div>
</header>
<section class="banner">
  <svg class="banner-art" width="1200" height="292" viewBox="0 0 1200 292">
    <defs>
      <linearGradient id="board" x1="0" x2="1">
        <stop offset="0" stop-color="#1f2a22"/><stop offset=".6" stop-color="#3c5a47"/><stop offset="1" stop-color="#8aa07a"/>
      </linearGradient>
    </defs>
    <polygon role="img" aria-label="Close-up photo of a circuit board with a DIP switch and resistor" points="324,0 1140,0 1140,244 554,244" fill="url(#board)"/>
  </svg>
  <div class="org-title">MEASUREMENT INTEGRITY<br>REVIEW BOARD</div>
</section>
<div class="logo-box"><span class="logo-name">mirb</span></div>
<nav class="nav">
  <a href="#">OVERVIEW</a><a href="#">STATEMENT OF PURPOSE</a><a href="#">TYPES OF TESTING</a><a href="#">MEMBERS</a><a href="#">MEMBER LISTING</a><a href="#">CONTACTS</a><a href="#">LINKS</a>
</nav>
<div class="rule"></div>
<main class="content">
  <h2 class="section-head welcome-head">WELCOME TO THE WEBSITE</h2>
  <div class="intro">
    <p>The Measurement Integrity Review Board of Australia (MIRB) was established in 1995 to foster the growth of a professional and value adding compliance testing resource to serve the needs of Australian industry.</p>
    <p>MIRB is an incorporated association formed by NRLA accredited electrical testing laboratories in Australia and includes an accredited member from New Zealand. The association has 14 active members which operate laboratories in a total of 18 locations in Australia and New Zealand. The members provide testing services to the public in the areas of electrical safety, electromagnetic compatibility, electromagnetic radiation, electromedical equipment, energy efficiency labelling, environmental performance, gas appliances, lighting equipment, performance ratings, and telecommunications. The NRLA accreditation mark is shown below.</p>
    <p>The Association operates a paid secretariat to service the interests of its members and to provide information about the services available to the public from its members. The registered office is in Fitzroy, Victoria. The members of MIRB meet regularly to discuss issues of interest to its members and the testing industry and to make submissions to regulators, public investigations, inquiries and industry surveys. The Association nominates members to serve on relevant Committees of the National Standards Council and to make representations to government inquiries.</p>
    <p>Member laboratories of MIRB test equipment to Australian and International Standards so that the clients are able to apply the appropriate regulatory mark for their product. The commonly recognised regulatory marks are the C-Tick and A-Tick for Australia, CE for Europe, FCC for the USA as shown below.</p>
  </div>
  <h2 class="section-head members-head">MEMBERS</h2>
  <div class="tile" style="left:735px;top:84px">Orbtest</div>
  <div class="tile" style="left:902px;top:84px">Coraline Labs</div>
  <div class="tile" style="left:735px;top:190px">Vantest</div>
  <div class="tile" style="left:902px;top:190px"><i></i>Fieldline</div>
  <div class="tile" style="left:735px;top:299px;color:#2b2b2b">Gridwell</div>
  <div class="tile" style="left:902px;top:299px;color:#b0123a">Voltaris</div>
</main>
<footer class="footer">
  Copyright © 2012 mirb<br>
  home | overview | statement of purpose | types of testing | members details<br>
  member geographical | contact | links | site map
</footer>
<div class="marks">
  <svg width="30" height="40"><polygon points="15,2 28,20 15,38 2,20" fill="#111"/></svg>
  <svg width="32" height="40"><circle cx="16" cy="20" r="15" fill="#111"/></svg>
  <svg width="38" height="40"><polygon points="19,4 36,36 2,36" fill="none" stroke="#111" stroke-width="3"/></svg>
  <svg width="38" height="40"><rect x="3" y="7" width="32" height="26" fill="#111"/></svg>
  <svg width="40" height="40"><rect x="2" y="5" width="36" height="30" fill="#111"/></svg>
</div>
</body>
</html>
```